One page front and back healthcare law brochure

Our small law firm provides legal services to businesses in the health care industry. We would like a single page 8.5x11 front and back brochure that highlights the services we offer. The intent of the brochure is to communicate our professionalism, high work quality, and depth of experience in healthcare law.
Target Market(s)
Doctors, Hospitals, Medical practices, Dental practices, Healthcare clinics, Healthcare tech companies, Healthcare entrepreneurs, Nurses, Med Spas, Pain Management Clinics, Weight Loss Clinics
Industry/Entity Type
Legal, Healthcare
Requirements
Nice to have
- Visually align with https://tovin.law/ and https://tovin.law/health-care/

```html
<!DOCTYPE html>
<html lang="en">
<head>
<meta charset="utf-8">
<title>TOVIN.LAW Healthcare Law Brochure</title>
<link href="https://fonts.googleapis.com/css2?family=Montserrat:wght@400;500;600;700;800&display=swap" rel="stylesheet">
<style>
  :root {
    --stage: #e1e1e3;
    --paper: #ffffff;
    --blue: #1f5fae;
    --blue-deep: #1a4f97;
    --yellow: #f7ec33;
    --ink: #3a3f47;
    --ink-soft: #5b6069;
    --photo-dark: #15384f;
    --photo-mid: #3f7d98;
    --photo-light: #9cc4d1;
  }
  * { box-sizing: border-box; margin: 0; padding: 0; }
  html, body { width: 1200px; height: 935px; overflow: hidden; }
  body {
    background: var(--stage);
    font-family: "Montserrat", sans-serif;
    color: var(--ink);
    position: relative;
  }
  .sheet {
    position: absolute;
    top: 105px;
    width: 560px;
    height: 725px;
    background: var(--paper);
    box-shadow: 0 12px 30px rgba(0,0,0,0.15);
    overflow: hidden;
  }
  .sheet--back { left: 30px; }
  .sheet--front { left: 610px; }

  /* ---------- Front ---------- */
  .masthead {
    height: 62px;
    display: flex;
    align-items: center;
    gap: 16px;
  }
  .masthead__rule { flex: 1; height: 6px; background: var(--blue); }
  .firm-name {
    font-weight: 600;
    font-size: 18px;
    letter-spacing: 1px;
    line-height: 1;
    color: var(--ink);
  }

  .hero-photo {
    margin: 0 22px;
    height: 178px;
    background: linear-gradient(115deg, var(--photo-light) 0%, var(--photo-mid) 35%, var(--photo-dark) 75%, #0e2536 100%);
  }
  .intro {
    background: var(--yellow);
    margin: 0 22px;
    padding: 18px 26px 16px;
  }
  .intro__row { display: flex; align-items: stretch; gap: 22px; }
  .intro__title {
    width: 200px;
    flex: none;
    font-weight: 800;
    font-size: 20px;
    line-height: 1.15;
    color: var(--ink);
  }
  .intro__title em { font-style: normal; color: var(--blue); }
  .intro__divider { width: 1px; background: #b9b12a; }
  .intro__text { flex: 1; font-size: 8px; line-height: 1.45; color: var(--ink); align-self: center; }
  .intro__heading {
    margin-top: 16px;
    font-size: 16px;
    font-weight: 800;
    color: var(--blue);
    letter-spacing: 0.2px;
    white-space: nowrap;
  }
  .body-copy {
    padding: 14px 44px 0;
    font-size: 7.6px;
    line-height: 1.5;
    color: var(--ink-soft);
  }
  .body-copy p + p { margin-top: 9px; }
  .front-base {
    position: absolute; left: 22px; right: 22px; bottom: 22px;
    height: 14px; background: var(--blue);
  }

  /* ---------- Back ---------- */
  .expertise { padding: 44px 36px 0; }
  .expertise__title {
    text-align: center; font-size: 24px; font-weight: 700; color: var(--ink);
    margin-bottom: 22px;
  }
  .expertise__row { display: flex; justify-content: center; }
  .expertise__row + .expertise__row { margin-top: 22px; }
  .service { width: 150px; padding: 0 14px; text-align: center; }
  .service + .service { border-left: 1.5px solid var(--yellow); }
  .service__head { display: flex; align-items: center; justify-content: center; gap: 6px; margin-bottom: 8px; min-height: 30px; }
  .service__icon { width: 22px; height: 22px; flex: none; }
  .service__name { font-size: 8px; font-weight: 700; line-height: 1.25; text-align: left; color: var(--ink); }
  .service__text { font-size: 7px; line-height: 1.5; color: var(--ink-soft); }

  .why { padding: 38px 44px 0; }
  .why__title { font-size: 20px; font-weight: 800; color: var(--ink); margin-bottom: 10px; }
  .why__title em { font-style: normal; color: var(--blue); }
  .why__list { list-style: none; }
  .why__item { display: flex; gap: 6px; font-size: 8px; line-height: 1.45; margin-bottom: 5px; color: var(--ink); }
  .why__item svg { flex: none; margin-top: 2px; }
  .why__item strong { color: var(--blue); font-weight: 700; }

  .contact {
    position: absolute; left: 0; right: 0; bottom: 44px;
    height: 108px;
    background: var(--yellow);
    display: flex; align-items: center;
    padding: 0 44px;
  }
  .contact__col { flex: 1; }
  .contact__title { font-size: 16px; font-weight: 800; color: var(--blue); margin-bottom: 8px; }
  .contact__line { display: flex; align-items: center; gap: 7px; font-size: 8px; font-weight: 600; color: var(--ink); margin-top: 4px; }
  .contact__rule { width: 0; height: 64px; border-left: 1px dashed #b9b12a; margin: 0 30px; }
  .contact__address { display: flex; align-items: flex-start; gap: 8px; font-size: 8.5px; font-weight: 600; line-height: 1.4; color: var(--ink); }
  .back-base { position: absolute; left: 0; right: 0; bottom: 22px; height: 12px; background: var(--blue-deep); }
</style>
</head>
<body>

<section class="sheet sheet--back" aria-label="Brochure back">
  <div class="expertise">
    <h2 class="expertise__title">Our Expertise</h2>
    <div class="expertise__row">
      <div class="service">
        <div class="service__head">
          <svg class="service__icon" viewBox="0 0 24 24" fill="none" stroke="#f2d51d" stroke-width="1.6"><path d="M5 3v6a5 5 0 0 0 10 0V3"/><path d="M10 14v3a4 4 0 0 0 8 0v-2"/><circle cx="18" cy="13" r="2"/></svg>
          <span class="service__name">Medical<br>Practices</span>
        </div>
        <p class="service__text">Navigating the intricate landscape of healthcare regulations, regulatory compliance, and business legal issues. We ensure that your practice operates smoothly while avoiding costly legal pitfalls.</p>
      </div>
      <div class="service">
        <div class="service__head">
          <svg class="service__icon" viewBox="0 0 24 24" fill="none" stroke="#f2d51d" stroke-width="1.6"><path d="M12 3l7 3v5c0 5-3 8-7 10-4-2-7-5-7-10V6z"/></svg>
          <span class="service__name">Med Spas</span>
        </div>
        <p class="service__text">Guiding med spas through confusing and ever-changing regulations, licensing, and compliance issues while ensuring their operations are legally sound.</p>
      </div>
      <div class="service">
        <div class="service__head">
          <svg class="service__icon" viewBox="0 0 24 24" fill="none" stroke="#f2d51d" stroke-width="1.6"><rect x="4" y="4" width="12" height="14" rx="1.5"/><path d="M8 9h4M10 7v4M16 10h4v8h-6"/></svg>
          <span class="service__name">Medical Device<br>Companies</span>
        </div>
        <p class="service__text">Providing counsel on regulatory compliance, intellectual property, product liability, and contracts to help device manufacturers succeed in a competitive marketplace.</p>
      </div>
    </div>
    <div class="expertise__row">
      <div class="service">
        <div class="service__head">
          <svg class="service__icon" viewBox="0 0 24 24" fill="none" stroke="#f2d51d" stroke-width="1.6"><rect x="4" y="8" width="9" height="12" rx="2"/><path d="M6 8V5h5v3"/><circle cx="17" cy="15" r="3.5"/></svg>
          <span class="service__name">Weight Loss and<br>Pain Management<br>Clinics</span>
        </div>
        <p class="service__text">Offering guidance and support on compliance, licensing, and patient care and safety to ensure exceptional care while adhering to strict regulatory standards.</p>
      </div>
      <div class="service">
        <div class="service__head">
          <svg class="service__icon" viewBox="0 0 24 24" fill="none" stroke="#f2d51d" stroke-width="1.6"><rect x="3" y="5" width="18" height="11" rx="1.5"/><path d="M9 20h6M12 16v4M9 10h6M12 8v4"/></svg>
          <span class="service__name">Medical Software<br>Companies</span>
        </div>
        <p class="service__text">Addressing the unique legal needs of software companies in healthcare, including data privacy, cybersecurity, and regulatory compliance.</p>
      </div>
    </div>
  </div>

  <div class="why">
    <h2 class="why__title">Why Choose <em>TOVIN.LAW?</em></h2>
    <ul class="why__list">
      <li class="why__item"><svg width="9" height="9" viewBox="0 0 10 10"><circle cx="5" cy="5" r="4.3" fill="none" stroke="#1f5fae"/><path d="M3 5.2l1.4 1.4L7.2 3.8" fill="none" stroke="#1f5fae" stroke-width="1.1"/></svg><span><strong>Industry-Focused:</strong> Our deep understanding of the healthcare sector enables us to provide tailored legal solutions.</span></li>
      <li class="why__item"><svg width="9" height="9" viewBox="0 0 10 10"><circle cx="5" cy="5" r="4.3" fill="none" stroke="#1f5fae"/><path d="M3 5.2l1.4 1.4L7.2 3.8" fill="none" stroke="#1f5fae" stroke-width="1.1"/></svg><span><strong>Experienced Team:</strong> Our HIPAA certified attorneys have extensive experience in healthcare law, delivering effective counsel and representation.</span></li>
      <li class="why__item"><svg width="9" height="9" viewBox="0 0 10 10"><circle cx="5" cy="5" r="4.3" fill="none" stroke="#1f5fae"/><path d="M3 5.2l1.4 1.4L7.2 3.8" fill="none" stroke="#1f5fae" stroke-width="1.1"/></svg><span><strong>Proactive Approach:</strong> We anticipate challenges before they arise, providing strategic advice to safeguard your business.</span></li>
      <li class="why__item"><svg width="9" height="9" viewBox="0 0 10 10"><circle cx="5" cy="5" r="4.3" fill="none" stroke="#1f5fae"/><path d="M3 5.2l1.4 1.4L7.2 3.8" fill="none" stroke="#1f5fae" stroke-width="1.1"/></svg><span><strong>Comprehensive Services:</strong> From compliance to drafting legal documents to dispute resolution, we offer end-to-end legal support for most healthcare law needs.</span></li>
    </ul>
  </div>

  <div class="contact">
    <div class="contact__col">
      <div class="contact__title">Contact Us Today</div>
      <div class="contact__line"><svg width="12" height="12" viewBox="0 0 12 12"><circle cx="6" cy="6" r="6" fill="#1f5fae"/><path d="M4 3.2l1 1.4-.6.7a4 4 0 0 0 2.3 2.3l.7-.6 1.4 1-.6 1C5.8 9 3 6.2 3 3.8z" fill="#fff"/></svg>(555) 014-0188</div>
      <div class="contact__line"><svg width="12" height="12" viewBox="0 0 12 12"><circle cx="6" cy="6" r="6" fill="#1f5fae"/><rect x="3" y="4" width="6" height="4.2" fill="#fff"/><path d="M3 4l3 2.3L9 4" fill="none" stroke="#1f5fae" stroke-width=".7"/></svg>info@tovin.law</div>
    </div>
    <div class="contact__rule"></div>
    <div class="contact__col">
      <div class="contact__address"><svg width="14" height="14" viewBox="0 0 14 14"><circle cx="7" cy="7" r="7" fill="#1f5fae"/><path d="M7 3a2.6 2.6 0 0 0-2.6 2.6C4.4 7.6 7 11 7 11s2.6-3.4 2.6-5.4A2.6 2.6 0 0 0 7 3z" fill="#fff"/><circle cx="7" cy="5.6" r="1" fill="#1f5fae"/></svg><span>418 Harlow Street, Suite 120<br>Brookfield, NC, 28000</span></div>
    </div>
  </div>
  <div class="back-base"></div>
</section>

<section class="sheet sheet--front" aria-label="Brochure front">
  <header class="masthead">
    <div class="masthead__rule"></div>
    <span class="firm-name">TOVIN.LAW</span>
    <div class="masthead__rule"></div>
  </header>

  <div class="hero-photo" role="img" aria-label="Photo of a businessman touching a rising bar chart with an upward arrow on a digital screen"></div>

  <div class="intro">
    <div class="intro__row">
      <h1 class="intro__title">YOUR <em>TRUSTED</em><br>PARTNER IN<br>HEALTHCARE<br>LAW</h1>
      <div class="intro__divider"></div>
      <p class="intro__text">At TOVIN.LAW, our dedicated Healthcare Law Practice Group is committed to safeguarding the interests of healthcare businesses like yours. Our team understands the unique challenges of this highly regulated industry. We are experienced in navigating the complexities of healthcare law to protect your business, allowing you to focus on what you do best: delivering exceptional care.</p>
    </div>
    <h2 class="intro__heading">PROTECTING &amp; HELPING YOUR BUSINESS GROW</h2>
  </div>

  <div class="body-copy">
    <p>Whether you're starting a new business or managing an established enterprise, the focus of your attention and energy is on developing and commercializing your practice, products, and/or services. Due to time constraints and the overwhelming amount of work your business requires, proper legal planning sometimes takes a back seat. We can help. TOVIN.LAW seeks to relieve the stress and anxiety associated with unaddressed legal issues by handling these challenges and allowing our clients to focus on growing their companies.</p>
    <p>Our Healthcare Law practice encompasses a wide range of services. We guide clients through the proper establishment of new businesses, and the myriad issues that arise as companies interact with the public, other companies, regulatory bodies, and the government. We help make sure businesses are correctly organized and comply with state and federal laws, rules, and regulations pertaining to raising capital, acquiring other businesses or assets, protecting patient information, complying with health law regulations and statutes, and adding and removing owners.</p>
    <p>Buying a healthcare business, cementing a strategic partnership, and executing an exit event are all fraught with pitfalls and unexpected risks. When a deal or contract needs to get negotiated, documented, and closed – we excel. We fight to get the right deal terms for our clients and offer creative solutions to help navigate these minefields and achieve a successful result.</p>
    <p>We work with all forms of businesses including partnerships, limited liability companies (LLCs), and corporations. Regardless of the type of business, it is imperative that the potential legal threats and obstacles the business may face are properly addressed.</p>
  </div>
  <div class="front-base"></div>
</section>

</body>
</html>
```